an author seeking a cool ebook cover design

We need an ebook cover design for an old book I'd written 10yrs ago so that I can make it into an ebook. It's a self help health and wellbeing book, that covers everything from fitness, nutrition to mediation and stress management.

I'd like to see designs that use a toolbox (i have attached a photo I'd like to use (no need for stock photo as it's my toolbox and photo).

The cover should be clear and easy to read.

here's a description of what's inside the book (i've also attached a rough pdf of insides)
Marrow Quiet Ledger is full of all the practical tips you need to help get you thinking straight, feeling great and looking great.

This concise books saves you time by finding the right tool you need for your own personal challenge, be it physical, mental or energetic. It’s practical, fun, easy to read and most of all it’s effective.

Arto Pimbley brings all his experience and knowledge and bundles it all together to give you a book that is in many ways the ‘evening almanac’ on lifestyle! It will help you turn every day dramas and challenges into remarkable successes.

The three main parts to this book are essential to living: The mind, the body and the spirit. You will learn how to meditate, stretch, exercise, eat well to live longer, choose a new direction in life, deal with stress, use acupressure for illness and learn how to clear a cluttered mind and transform it into a happy and content one.

Target Market(s)

25- 40yr old mostly female

Industry/Entity Type

Nutrition

Requirements
Must have
• must have:
the author name - Arto Pimbley
Book title - Marrow Quiet Ledger
bi line - quick tips for a happier healthier you
picture of toolbox
must have specs:

1,600 pixels wide by 2,400 pixels tall or similar ratio. The image must be at least 1,600 pixels wide, and the height should be greater than the width.
image must be in RGB color, not CMYK
file type to be jpeg - maximum file size 18MB
Nice to have
• like to see more of hand written font style like 'sketch nice' if possible

```html
<!DOCTYPE html>
<html lang="en">
<head>
<meta charset="utf-8">
<title>Marrow Quiet Ledger — ebook cover</title>
<link rel="stylesheet" href="https://fonts.googleapis.com/css2?family=Cabin+Sketch:wght@700&family=Special+Elite&family=Oswald:wght@500&display=swap">
<style>
  :root {
    --sky-top: #4fb6e6;
    --sky-mid: #bfe6f6;
    --glow: #ffffff;
    --meadow: #c5e07a;
    --meadow-deep: #8cc43f;
    --grass-dark: #4f9a1f;
    --grass-light: #9fd24a;
    --title-red: #e2342b;
    --box-red: #d8322a;
    --box-shadow: #8e1c17;
    --ink: #3b3b3b;
  }
  html, body {
    margin: 0;
    padding: 0;
    overflow: hidden;
  }
  .cover {
    position: relative;
    width: 800px;
    height: 1200px;
    overflow: hidden;
    background:
      radial-gradient(circle at 62% 36%, var(--glow) 0%, rgba(255,255,255,0.85) 18%, rgba(255,255,255,0) 45%),
      linear-gradient(180deg, var(--sky-top) 0%, var(--sky-mid) 30%, #eef8ec 50%, var(--meadow) 72%, var(--meadow-deep) 100%);
  }
  .title {
    position: absolute;
    top: 70px;
    left: 0;
    width: 100%;
    margin: 0;
    text-align: center;
    font-family: "Cabin Sketch", cursive;
    font-weight: 700;
    font-size: 150px;
    line-height: 150px;
    color: var(--title-red);
    letter-spacing: 2px;
  }
  .title span { display: block; }
  .tagline {
    position: absolute;
    top: 545px;
    left: 0;
    width: 100%;
    margin: 0;
    text-align: center;
    font-family: "Special Elite", monospace;
    font-size: 34px;
    color: var(--ink);
  }
  .toolbox {
    position: absolute;
    left: 250px;
    top: 670px;
    width: 410px;
    height: 250px;
  }
  .byline {
    position: absolute;
    top: 990px;
    left: 0;
    width: 100%;
    text-align: center;
  }
  .byline-label {
    display: block;
    font-family: "Special Elite", monospace;
    font-size: 22px;
    color: var(--ink);
  }
  .author {
    display: block;
    margin-top: 2px;
    font-family: "Oswald", sans-serif;
    font-weight: 500;
    font-size: 64px;
    line-height: 72px;
    color: var(--title-red);
  }
  .grass {
    position: absolute;
    left: 0;
    bottom: 0;
    width: 800px;
    height: 120px;
    background: linear-gradient(180deg, var(--grass-light) 0%, var(--grass-dark) 100%);
  }
</style>
</head>
<body>
  <div class="cover">
    <h1 class="title"><span>Marrow</span><span>Quiet</span><span>Ledger</span></h1>
    <p class="tagline">quick tips for a happier healthier you</p>

    <svg class="toolbox" viewBox="0 0 410 250" role="img" aria-label="Photo of the author's red metal toolbox with its lid slightly open">
      <ellipse cx="205" cy="238" rx="200" ry="12" fill="var(--box-shadow)" opacity="0.25"/>
      <rect x="0" y="20" width="410" height="215" rx="10" fill="var(--box-red)"/>
    </svg>

    <div class="byline">
      <span class="byline-label">written and illustrated by</span>
      <span class="author">Arto Pimbley</span>
    </div>

    <div class="grass" role="img" aria-label="Photo of fresh green grass along the bottom edge"></div>
  </div>
</body>
</html>
```